Software Architecture Drawing

I have a software architecture that we would like to pretty up. Our current drawing was done in VISIO, but it just doesn't look professional (and salesy) enough. We would like an illustration that is attractive, makes simple use of colour, and allows us to make little tweaks (wording, etc.). We used icons for certain concepts, but these will have to be redrawn (or purchased). This particular software application is able to receive many data points, store it in a high performance data store, and make it available to various users for analysis or other systems for other purposes

Target Market(s)

Software Architects, IT Professionals

Industry/Entity Type

Software

Font styles to use
Sans Serif

Colors
0355a3
3176b5
85acd3
cedeec
f37022
f68e4e

Requirements
Must have
• Unique (or legal copies) of logos to represent various input sources.

```html
<!DOCTYPE html>
<html lang="en">
<head>
<meta charset="utf-8">
<title>Data Platform Architecture</title>
<link rel="stylesheet" href="https://fonts.googleapis.com/css2?family=Open+Sans:wght@400;600&display=swap">
<style>
  :root{
    --blue-dark:#0355a3;
    --blue:#3176b5;
    --blue-light:#85acd3;
    --blue-pale:#cedeec;
    --orange:#f37022;
    --orange-light:#f68e4e;
    --cream:#f4f0e4;
    --cream-edge:#e9e3cf;
    --arrow:#d5d1bf;
    --mauve:#c28a78;
    --white:#ffffff;
    --shade:#7aa8da;
  }
  *{box-sizing:border-box;margin:0;padding:0}
  html,body{width:1200px;height:900px;overflow:hidden}
  body{font-family:"Open Sans",Arial,sans-serif;color:var(--white)}
  .canvas{position:relative;width:1200px;height:900px;overflow:hidden;
    background:radial-gradient(ellipse at 40% 45%,#faf8f1 0%,var(--cream) 55%,var(--cream-edge) 100%)}
  .abs{position:absolute}
  .arrows{position:absolute;left:0;top:0}
  .arrows .a{fill:var(--arrow)}

  .sources-title{left:170px;top:64px;font-size:17px;font-weight:400;color:var(--blue)}
  .source{position:absolute;left:190px;width:78px;text-align:center}
  .source-icon{display:block;margin:0 auto;width:38px;height:38px;background:var(--orange)}
  .source-label{display:block;margin-top:3px;font-size:11.5px;color:var(--blue)}

  .ingest-bar{left:315px;top:93px;width:50px;height:480px;background:var(--orange-light)}
  .vertical-label{position:absolute;left:50%;top:50%;white-space:nowrap;font-size:15px;
    transform:translate(-50%,-50%) rotate(-90deg)}

  .framework{left:449px;top:92px;width:246px;height:481px;background:var(--blue-light)}
  .framework-caption{position:absolute;left:0;right:0;top:428px;text-align:center;font-size:12.5px;line-height:16px}
  .utility{left:507px;top:92px;width:188px;height:413px;background:var(--blue-dark);
    border-left:4px solid var(--white);border-bottom:4px solid var(--white)}
  .utility-title{position:absolute;left:22px;top:175px;font-size:15px;line-height:18px}

  .viz-bar{left:779px;top:223px;width:50px;height:346px;background:var(--mauve)}

  .tile{left:903px;width:124px;height:82px;border:2px solid var(--arrow);background:rgba(255,255,255,.25)}
  .tile-unknown{top:92px;display:flex;align-items:center;justify-content:center;
    font-size:62px;font-weight:600;color:#9c6c5c;line-height:1}
  .tile-bars{top:225px}
  .tile-map{top:358px;padding:10px}
  .map-fill{width:100%;height:100%;background:linear-gradient(90deg,var(--blue) 0%,var(--blue-dark) 60%,var(--blue) 100%);border-radius:14px;opacity:.8}
  .tile-table{top:490px}

  .services{left:367px;top:655px;width:409px;height:50px;background:var(--blue);
    display:flex;align-items:center;justify-content:center;font-size:15.5px}
  .client{top:775px;width:104px;height:56px;display:flex;align-items:center;justify-content:center;
    text-align:center;font-size:12.5px;line-height:15px}
  .client-presentment{left:367px;background:var(--blue-dark)}
  .client-conservation{left:520px;background:var(--blue)}
  .client-custom{left:672px;background:var(--blue)}

  .shade{left:600px;top:0;width:600px;height:900px;background:var(--shade);mix-blend-mode:multiply;pointer-events:none}
</style>
</head>
<body>
<main class="canvas">

  <svg class="arrows" width="1200" height="900" viewBox="0 0 1200 900" aria-hidden="true">
    <g class="a">
      <polygon points="262,107 288,107 288,101 302,111 288,121 288,115 262,115"/>
      <polygon points="262,174 276,164 276,170 288,170 288,164 302,174 288,184 288,178 276,178 276,184"/>
      <polygon points="262,237 276,227 276,233 288,233 288,227 302,237 288,247 288,241 276,241 276,247"/>
      <polygon points="262,301 276,291 276,297 288,297 288,291 302,301 288,311 288,305 276,305 276,311"/>
      <polygon points="262,364 276,354 276,360 288,360 288,354 302,364 288,374 288,368 276,368 276,374"/>
      <polygon points="262,423 288,423 288,417 302,427 288,437 288,431 262,431"/>
      <polygon points="262,486 288,486 288,480 302,490 288,500 288,494 262,494"/>
      <polygon points="262,549 288,549 288,543 302,553 288,563 288,557 262,557"/>
      <polygon points="377,275 405,275 405,260 437,292 405,325 405,310 377,310"/>
      <polygon points="437,355 409,355 409,340 377,372 409,405 409,390 437,390"/>
      <polygon points="715,128 860,128 860,119 890,132 860,145 860,136 715,136"/>
      <polygon points="702,397 722,382 722,392 752,392 752,382 772,397 752,412 752,402 722,402 722,412"/>
      <polygon points="843,261 873,261 873,254 893,266 873,278 873,271 843,271"/>
      <polygon points="843,395 873,395 873,388 893,400 873,412 873,405 843,405"/>
      <polygon points="843,526 873,526 873,519 893,531 873,543 873,536 843,536"/>
      <polygon points="555,583 585,583 585,613 600,613 570,643 540,613 555,613"/>
      <polygon points="413,713 423,713 423,740 432,740 418,765 404,740 413,740"/>
      <polygon points="566,713 576,713 576,740 585,740 571,765 557,740 566,740"/>
      <polygon points="719,713 729,713 729,740 738,740 724,765 710,740 719,740"/>
    </g>
  </svg>

  <h2 class="abs sources-title">Data Sources</h2>

  <div class="source" style="top:93px">
    <svg class="source-icon" viewBox="0 0 38 38" aria-hidden="true"><circle cx="16" cy="19" r="2.6" fill="#fff"/><path d="M20 14a7 7 0 0 1 0 10M23 11a11 11 0 0 1 0 16" stroke="#fff" stroke-width="2.2" fill="none"/></svg>
    <span class="source-label">Special</span>
  </div>
  <div class="source" style="top:156px">
    <svg class="source-icon" viewBox="0 0 38 38" aria-hidden="true"><g fill="#fff"><rect x="8" y="9" width="14" height="2.4"/><rect x="8" y="14" width="12" height="2.4"/><rect x="8" y="19" width="8" height="2.4"/><circle cx="24" cy="24" r="6"/></g><circle cx="24" cy="24" r="2.3" fill="#f37022"/><g stroke="#fff" stroke-width="2.4"><path d="M24 15.5v3M24 29.5v3M15.5 24h3M29.5 24h3"/></g></svg>
    <span class="source-label">Operational</span>
  </div>
  <div class="source" style="top:218px">
    <svg class="source-icon" viewBox="0 0 38 38" aria-hidden="true"><g fill="#fff"><rect x="8" y="8" width="6" height="8"/><rect x="8" y="22" width="6" height="8"/><rect x="24" y="8" width="6" height="8"/><rect x="24" y="22" width="6" height="8"/><rect x="16" y="15" width="6" height="8" rx="2"/></g><path d="M14 19h10M11 16v6M27 16v6" stroke="#fff" stroke-width="1.6"/></svg>
    <span class="source-label">Enterprise</span>
  </div>
  <div class="source" style="top:282px">
    <svg class="source-icon" viewBox="0 0 38 38" aria-hidden="true"><g fill="#fff"><circle cx="12" cy="15" r="3"/><circle cx="19" cy="13" r="3.4"/><circle cx="26" cy="15" r="3"/><path d="M7 26c0-5 3-7 5-7s4 1 4 3v4zM14 26c0-6 3-9 5-9s5 3 5 9zM22 26v-4c0-2 2-3 4-3s5 2 5 7z"/></g></svg>
    <span class="source-label">Customer</span>
  </div>
  <div class="source" style="top:346px">
    <svg class="source-icon" viewBox="0 0 38 38" aria-hidden="true"><path d="M6 19 19 8l13 11h-4v11h-6v-7h-6v7h-6V19z" fill="#fff"/></svg>
    <span class="source-label">Property</span>
  </div>
  <div class="source" style="top:408px">
    <svg class="source-icon" viewBox="0 0 38 38" aria-hidden="true"><g stroke="#fff" stroke-width="2" fill="none"><circle cx="19" cy="19" r="11"/><ellipse cx="19" cy="19" rx="5" ry="11"/><path d="M8 19h22M10 13h18M10 25h18"/></g></svg>
    <span class="source-label">Geospatia</span>
  </div>
  <div class="source" style="top:472px">
    <svg class="source-icon" viewBox="0 0 38 38" aria-hidden="true"><path d="M8 10h22v14H17l-6 5v-5H8z" fill="#fff"/></svg>
    <span class="source-label">Social Media</span>
  </div>
  <div class="source" style="top:535px">
    <svg class="source-icon" viewBox="0 0 38 38" aria-hidden="true"><circle cx="14" cy="14" r="4" fill="#fff"/><path d="M14 6v2M6 14h2M8.5 8.5l1.5 1.5M19.5 8.5 18 10" stroke="#fff" stroke-width="1.6" fill="none"/><path d="M13 24a4 4 0 0 1 4-6 6 6 0 0 1 11 2 3 3 0 0 1 0 6H16a3 3 0 0 1-3-2z" fill="#fff"/><path d="M16 29l-1 3M21 29l-1 3M26 29l-1 3" stroke="#fff" stroke-width="1.6" fill="none"/></svg>
    <span class="source-label">Weather</span>
  </div>

  <div class="abs ingest-bar"><span class="vertical-label">Some Text About Here</span></div>

  <section class="abs framework">
    <p class="framework-caption">Verano Low-Latency<br>Transaction Execution Framework</p>
  </section>
  <div class="abs utility"><p class="utility-title">High-Performance<br>Sensational<br>Utility</p></div>

  <div class="abs viz-bar"><span class="vertical-label">All sorts of Visualization Tools</span></div>

  <div class="abs tile tile-unknown">?</div>

  <div class="abs tile tile-bars">
    <svg width="120" height="78" viewBox="0 0 120 78" aria-label="Bar chart">
      <g stroke="#c9c6b6" stroke-width="0.6" fill="none">
        <path d="M18 10v56h92"/>
        <path d="M18 24h92M18 38h92M18 52h92" stroke-dasharray="2 2"/>
      </g>
      <rect x="26" y="53" width="14" height="13" fill="#85acd3"/>
      <rect x="46" y="32" width="14" height="34" fill="#a17a70"/>
      <rect x="66" y="42" width="14" height="24" fill="#3176b5"/>
      <rect x="86" y="18" width="14" height="48" fill="#a17a70"/>
    </svg>
  </div>

  <div class="abs tile tile-map"><div class="map-fill" role="img" aria-label="World map with highlighted locations"></div></div>

  <div class="abs tile tile-table">
    <svg width="120" height="78" viewBox="0 0 120 78" aria-label="Data table">
      <g fill="#cedeec">
        <rect x="8" y="6" width="34" height="6" fill="#0355a3"/><rect x="46" y="6" width="36" height="6" fill="#0355a3"/><rect x="86" y="6" width="24" height="6" fill="#0355a3"/>
        <rect x="8" y="16" width="34" height="6" fill="#a17a70"/><rect x="46" y="16" width="36" height="6"/><rect x="46" y="16" width="34" height="6" fill="#a17a70"/><rect x="86" y="16" width="24" height="6"/>
        <rect x="8" y="26" width="34" height="6" fill="#a17a70"/><rect x="46" y="26" width="36" height="6"/><rect x="46" y="26" width="22" height="6" fill="#a17a70"/><rect x="86" y="26" width="24" height="6"/>
        <rect x="8" y="36" width="34" height="6" fill="#0355a3"/><rect x="46" y="36" width="36" height="6"/><rect x="46" y="36" width="8" height="6" fill="#0355a3"/><rect x="86" y="36" width="24" height="6"/>
        <rect x="8" y="46" width="34" height="6"/><rect x="8" y="46" width="26" height="6" fill="#a17a70"/><rect x="46" y="46" width="36" height="6"/><rect x="86" y="46" width="24" height="6"/>
        <rect x="8" y="56" width="34" height="6"/><rect x="8" y="56" width="18" height="6" fill="#3176b5"/><rect x="46" y="56" width="36" height="6"/><rect x="86" y="56" width="24" height="6"/>
        <rect x="8" y="66" width="34" height="6"/><rect x="8" y="66" width="10" height="6" fill="#0355a3"/><rect x="46" y="66" width="36" height="6"/><rect x="86" y="66" width="24" height="6"/>
      </g>
    </svg>
  </div>

  <div class="abs services">Web Services</div>
  <div class="abs client client-presentment">Customer<br>Presentment</div>
  <div class="abs client client-conservation">Conservation<br>idea</div>
  <div class="abs client client-custom">Custom<br>Clients</div>

  <div class="abs shade" aria-hidden="true"></div>
</main>
</body>
</html>
```